Publishing company needs book cover for multi-author book

Copperfield Lane Publishing needs a book cover designed for a multi-author book called Harbor Lanterns: Unlikely Triumph Accounts from Remarkable Pioneers. We would like to see designs that incorporates the design theme of the image attached and possibly the image itself. The book will be used by the contributing authors who are  are Healers, Psychics, Coaches, Energy Workers, Astrologers, Numerologist, Tarot Card Readers and will be using this book to both market their business and use in their practices.  The final design should communicate  these spiritual practices.
I would love to see
1. A silhouette or image of a woman holding a ball or circle with the attached art inside of.
2. The concepts in the attached art brought into a  new design or  enhancing the original art.

Target Market(s)
The clients and audiences of the contributing authors
Industry/Entity Type
Spiritual, Body Mind Spirit, Evolving Continuousness, Alternative Healing
Colors
Designer to choose colors to be used in the design.
Requirements
Must have
- Title- Harbor Lanterns: Unlikely Triumph Accounts from Remarkable Pioneers. and the name of the publishing company: Copperfield Lane Publishing

Nice to have
- I would love to have the concept of the artwork coming to life through an image of woman, visionary, healer who is healing the world through her modalities.

Should not have
- Dimensions - 6X9

```html
<!DOCTYPE html>
<html lang="en">
<head>
<meta charset="utf-8">
<title>Harbor Lanterns – Book Cover</title>
<link href="https://fonts.googleapis.com/css2?family=Bebas+Neue&family=Great+Vibes&family=Lato:wght@700&family=Montserrat:wght@700&display=swap" rel="stylesheet">
<style>
  :root {
    --page-bg: #ffffff;
    --cover-navy: #050a1f;
    --glow-white: #f4fbff;
    --glow-pale: #9fdcff;
    --energy-blue: #2b5cff;
    --deep-blue: #0b1a8c;
    --text-white: #ffffff;
    --text-soft: #b9d6f2;
    --title-glow: #3fc4ff;
    --script-cyan: #4cc6ea;
    --script-cyan-light: #8fe3f7;
    --subtitle-halo: #2a43c9;
  }
  html, body {
    margin: 0;
    padding: 0;
    width: 1200px;
    height: 1200px;
    overflow: hidden;
    background: var(--page-bg);
  }
  .book-cover {
    position: absolute;
    left: 250px;
    top: 75px;
    width: 700px;
    height: 1050px;
    background: var(--cover-navy);
    overflow: hidden;
    box-shadow: 0 2px 8px rgba(0,0,0,0.25);
  }
  .cover-art {
    position: absolute;
    left: 0;
    top: 0;
    width: 700px;
    height: 500px;
    background:
      radial-gradient(ellipse 110px 150px at 345px 275px, var(--glow-white) 0%, rgba(159,220,255,0.9) 40%, rgba(159,220,255,0) 100%),
      radial-gradient(ellipse 420px 330px at 345px 270px, rgba(110,175,255,0.95) 0%, var(--energy-blue) 40%, #1a36c8 70%, var(--deep-blue) 100%),
      var(--deep-blue);
  }
  .cover-art::after {
    content: "";
    position: absolute;
    left: 0;
    bottom: 0;
    width: 100%;
    height: 110px;
    background: linear-gradient(to bottom, rgba(5,10,31,0) 0%, var(--cover-navy) 90%);
  }
  .subtitle {
    position: absolute;
    left: 0;
    top: 528px;
    width: 700px;
    margin: 0;
    text-align: center;
    font-family: 'Lato', sans-serif;
    font-weight: 700;
    font-size: 18px;
    line-height: 30px;
    letter-spacing: 4.6px;
    color: var(--text-white);
    text-transform: uppercase;
    text-shadow: 0 0 6px var(--subtitle-halo), 0 0 12px var(--subtitle-halo);
  }
  .title {
    position: absolute;
    left: 0;
    top: 650px;
    width: 700px;
    margin: 0;
    text-align: center;
  }
  .title-main {
    display: block;
    font-family: 'Bebas Neue', sans-serif;
    font-weight: 400;
    font-size: 172px;
    line-height: 150px;
    letter-spacing: 6px;
    color: var(--text-white);
    text-shadow: 0 0 6px var(--title-glow), 0 0 14px var(--title-glow);
  }
  .title-script {
    display: block;
    margin-top: -8px;
    font-family: 'Great Vibes', cursive;
    font-weight: 400;
    font-size: 128px;
    line-height: 130px;
    background: linear-gradient(to bottom, var(--script-cyan-light), var(--script-cyan));
    -webkit-background-clip: text;
    background-clip: text;
    color: transparent;
  }
  .author {
    position: absolute;
    left: 0;
    top: 972px;
    width: 700px;
    margin: 0;
    text-align: center;
    font-family: 'Montserrat', sans-serif;
    font-weight: 700;
    font-size: 29px;
    line-height: 36px;
    letter-spacing: 1.5px;
    color: var(--text-white);
    text-shadow: 2px 2px 2px rgba(0,0,0,0.6);
  }
  .publisher {
    position: absolute;
    left: 0;
    top: 1018px;
    width: 700px;
    margin: 0;
    text-align: center;
    font-family: 'Lato', sans-serif;
    font-weight: 700;
    font-size: 12px;
    line-height: 16px;
    letter-spacing: 3px;
    text-transform: uppercase;
    color: var(--text-soft);
  }
</style>
</head>
<body>
  <div class="book-cover">
    <div class="cover-art" role="img" aria-label="Silhouette of a meditating figure with raised joined hands, radiating bright blue energy light"></div>
    <p class="subtitle">Unlikely Triumph Accounts<br>from Remarkable Pioneers</p>
    <h1 class="title">
      <span class="title-main">HARBOR</span>
      <span class="title-script">Lanterns</span>
    </h1>
    <p class="author">AUTHOR NAME</p>
    <p class="publisher">Copperfield Lane Publishing</p>
  </div>
</body>
</html>
```